Home Design company focused on remodel and enhancement of kitchens and bathroorms

I already have a logo designed by ArtHarbor, I now need a design for my business cards.
The company is in the remodeling and enhancement industry for homes, focusing on kitchens and bathrooms, however, we can remodel or enhance every room in a home, an office space, etc.

The company's name is VELMOR HOME DESIGN, LLC

We'll focus on clients in the Rio Grande Valley, Texas. Primarily McAllen, Edinburg, Pharr, Mission, Brownsville and South Padre Island.

The design on the business card should transmit reliability, professionalism anda bit of upscale design.

The logo is in black and white, and would like to keep it that way.

The information that needs to be printed in the business cards is:
Company's name: Velmor Studio
Company's Logo (attached)
My name: Noel Bramwit
Address, phone and email:
2715 N Parkline Road, Ste 348
Corvale, TX 78599
(361) 555 0187
nbramwit@velmor.example
Website: velmor.example

```html
<!DOCTYPE html>
<html lang="en">
<head>
<meta charset="utf-8">
<title>Velmor Studio — Business Card</title>
<link href="https://fonts.googleapis.com/css2?family=Arimo:wght@400&display=swap" rel="stylesheet">
<style>
  :root {
    --backdrop: #d2d3d5;
    --paper: #ffffff;
    --ink: #111111;
    --rule: #b9b9b9;
    --reverse-paper: #000000;
    --reverse-ink: #ffffff;
  }
  * { margin: 0; padding: 0; box-sizing: border-box; }
  html, body { width: 1200px; height: 1199px; overflow: hidden; }
  body {
    background: var(--backdrop);
    font-family: "Arimo", Arial, sans-serif;
    position: relative;
  }
  .card {
    position: absolute;
    left: 286px;
    width: 588px;
    height: 353px;
  }
  .card--front { top: 165px; background: var(--paper); color: var(--ink); }
  .card--back { top: 648px; background: var(--reverse-paper); color: var(--reverse-ink); }

  .wordmark {
    position: absolute;
    left: 0; right: 0;
    display: flex;
    align-items: center;
    justify-content: center;
    gap: 14px;
  }
  .card--front .wordmark { top: 112px; }
  .card--back .wordmark { top: 156px; }
  .wordmark__square {
    width: 16px; height: 16px;
    background: currentColor;
  }
  .wordmark__name {
    font-size: 26px;
    letter-spacing: 7px;
    line-height: 1;
  }

  .divider {
    position: absolute;
    top: 176px; left: 26px; right: 28px;
    height: 1px;
    background: var(--rule);
  }
  .holder-name {
    position: absolute;
    top: 200px; left: 0; right: 0;
    text-align: center;
    font-size: 20px;
    font-weight: 400;
    letter-spacing: 0.3px;
  }
  .contact {
    position: absolute;
    font-size: 12.5px;
    line-height: 21px;
    display: flex;
    align-items: flex-start;
    gap: 10px;
  }
  .contact svg { flex: none; margin-top: 4px; }
  .contact--address { left: 82px; top: 247px; }
  .contact--address svg { margin-top: 12px; }
  .contact--phone { left: 80px; top: 293px; }
  .contact--email { left: 332px; top: 246px; }
  .contact--web { left: 332px; top: 270px; }

  .back-url {
    position: absolute;
    top: 292px; left: 0; right: 0;
    text-align: center;
    font-size: 13px;
    letter-spacing: 2px;
  }
</style>
</head>
<body>
  <section class="card card--front" aria-label="Business card front">
    <div class="wordmark">
      <span class="wordmark__square"></span>
      <span class="wordmark__name">VELMOR STUDIO</span>
    </div>
    <div class="divider"></div>
    <h1 class="holder-name">NOEL BRAMWIT</h1>

    <div class="contact contact--address">
      <svg width="12" height="16" viewBox="0 0 12 16" aria-hidden="true"><path d="M6 0C2.7 0 0 2.6 0 5.9 0 10.2 6 16 6 16s6-5.8 6-10.1C12 2.6 9.3 0 6 0zm0 8.2a2.3 2.3 0 1 1 0-4.6 2.3 2.3 0 0 1 0 4.6z" fill="currentColor"/></svg>
      <span>2715 N Parkline Road, Ste 348<br>Corvale, TX 78599</span>
    </div>
    <div class="contact contact--phone">
      <svg width="15" height="14" viewBox="0 0 24 24" aria-hidden="true"><path d="M6.6 10.8a15.1 15.1 0 0 0 6.6 6.6l2.2-2.2a1 1 0 0 1 1-.25 11.4 11.4 0 0 0 3.6.57 1 1 0 0 1 1 1V20a1 1 0 0 1-1 1A17 17 0 0 1 3 4a1 1 0 0 1 1-1h3.5a1 1 0 0 1 1 1c0 1.25.2 2.45.57 3.57a1 1 0 0 1-.25 1z" fill="currentColor"/></svg>
      <span>(361) 555 0187</span>
    </div>
    <div class="contact contact--email">
      <svg width="14" height="10" viewBox="0 0 14 10" aria-hidden="true"><rect width="14" height="10" fill="currentColor"/><path d="M0.5 0.5 7 5.5 13.5 0.5M0.5 9.5 5.2 4.6M13.5 9.5 8.8 4.6" stroke="#fff" stroke-width="1.1" fill="none"/></svg>
      <span>nbramwit@velmor.example</span>
    </div>
    <div class="contact contact--web">
      <svg width="12" height="12" viewBox="0 0 12 12" aria-hidden="true"><g fill="none" stroke="currentColor" stroke-width="1"><circle cx="6" cy="6" r="5.3"/><ellipse cx="6" cy="6" rx="2.4" ry="5.3"/><path d="M0.7 6h10.6M1.5 3.3h9M1.5 8.7h9"/></g></svg>
      <span>www.velmor.example</span>
    </div>
  </section>

  <section class="card card--back" aria-label="Business card back">
    <div class="wordmark">
      <span class="wordmark__square"></span>
      <span class="wordmark__name">VELMOR STUDIO</span>
    </div>
    <p class="back-url">www.velmor.example</p>
  </section>
</body>
</html>
```